Boat business cards

I'm looking for business cards with the two logos I've attached. I don't have an specific idea in mind and open to anything. All the usual info will be on the card. Name, position in company, nr, email, address, ect. The company rents out these two boats for charters and fishing.

```html
<!DOCTYPE html>
<html lang="en">
<head>
<meta charset="utf-8">
<title>Tide Runner Charters – Business Card</title>
<link rel="stylesheet" href="https://fonts.googleapis.com/css2?family=Montserrat:wght@400;500;800&display=swap">
<style>
  :root {
    --band-blue: #769dc8;
    --card-white: #ffffff;
    --page-white: #ffffff;
    --ink: #000000;
    --brand-grey: #5a5d63;
    --card-shadow: rgba(0, 0, 0, 0.35);
  }
  * { margin: 0; padding: 0; box-sizing: border-box; }
  html, body {
    width: 1200px;
    height: 1200px;
    overflow: hidden;
    background: var(--page-white);
    font-family: "Montserrat", sans-serif;
    color: var(--ink);
  }
  .canvas { position: relative; width: 1200px; height: 1200px; }
  .card {
    position: absolute;
    left: 237px;
    width: 697px;
    height: 408px;
    background: var(--card-white);
    box-shadow: -4px 8px 16px var(--card-shadow);
    overflow: hidden;
  }
  .card--front { top: 142px; }
  .card--back { top: 636px; }
  .card-bands { position: absolute; inset: 0; width: 100%; height: 100%; }
  .card-bands polygon { fill: var(--band-blue); }

  .holder-name {
    position: absolute; left: 35px; top: 86px;
    font-size: 24px; font-weight: 800; letter-spacing: 0.2px;
  }
  .holder-role {
    position: absolute; left: 35px; top: 119px;
    font-size: 19px; font-weight: 400;
  }
  .contact-list {
    position: absolute; left: 34px; top: 242px;
    list-style: none;
  }
  .contact-item {
    display: flex; align-items: center;
    height: 25.6px;
    font-size: 16px; font-weight: 500;
  }
  .contact-icon { width: 24px; height: 24px; margin-right: 8px; flex: none; }
  .web-line {
    position: absolute; left: 383px; top: 358px;
    display: flex; align-items: center;
    font-size: 16px; font-weight: 500;
  }
  .web-line .contact-icon { margin-right: 8px; }

  .brand-name {
    position: absolute;
    color: var(--brand-grey);
    font-weight: 800;
    white-space: nowrap;
    display: flex; align-items: center;
  }
  .brand-name--small { left: 462px; top: 76px; font-size: 30px; }
  .brand-name--large { left: 0; right: 0; top: 168px; justify-content: center; font-size: 52px; }
  .brand-dot {
    display: inline-block; border-radius: 50%;
    background: var(--band-blue); margin-right: 10px;
  }
  .brand-name--small .brand-dot { width: 16px; height: 16px; }
  .brand-name--large .brand-dot { width: 26px; height: 26px; margin-right: 16px; }
</style>
</head>
<body>
<div class="canvas">

  <section class="card card--front" aria-label="Business card front">
    <svg class="card-bands" viewBox="0 0 697 408" aria-hidden="true">
      <polygon points="0,0 444,0 320,61 0,61"/>
      <polygon points="377,347 697,347 697,408 253,408"/>
    </svg>

    <div class="brand-name brand-name--small"><span class="brand-dot"></span>Tide Runner</div>

    <h1 class="holder-name">Xxxxx Xxxxx</h1>
    <p class="holder-role">Xxxxxx</p>

    <ul class="contact-list">
      <li class="contact-item">
        <svg class="contact-icon" viewBox="0 0 24 24" aria-label="Address"><path d="M12 1a7 7 0 0 0-7 7c0 5 7 15 7 15s7-10 7-15a7 7 0 0 0-7-7zm0 9.5A2.5 2.5 0 1 1 12 5.5a2.5 2.5 0 0 1 0 5z"/></svg>
        <span>: xxxxxxxxxxxxxxxxxxxxx</span>
      </li>
      <li class="contact-item">
        <svg class="contact-icon" viewBox="0 0 24 24" aria-label="Phone"><path d="M6.6 10.8c1.4 2.8 3.8 5.1 6.6 6.6l2.2-2.2c.3-.3.7-.4 1-.2 1.1.4 2.3.6 3.6.6.6 0 1 .4 1 1V20c0 .6-.4 1-1 1C10.6 21 3 13.4 3 4c0-.6.4-1 1-1h3.5c.6 0 1 .4 1 1 0 1.3.2 2.5.6 3.6.1.3 0 .7-.2 1z"/></svg>
        <span>: xxx-xxx-xxxx</span>
      </li>
      <li class="contact-item">
        <svg class="contact-icon" viewBox="0 0 24 24" aria-label="Mobile"><rect x="7" y="2" width="10" height="20" rx="2" fill="none" stroke="#000" stroke-width="1.8" transform="rotate(18 12 12)"/></svg>
        <span>: xxx-xxx-xxxx</span>
      </li>
      <li class="contact-item">
        <svg class="contact-icon" viewBox="0 0 24 24" aria-label="Email"><path d="M1 5h22v14H1z"/><path d="M1 5l11 8 11-8M1 19l8-7M23 19l-8-7" fill="none" stroke="#fff" stroke-width="1.6"/></svg>
        <span>: xxxxxx@xxxxxxxxxxxx.xxx</span>
      </li>
    </ul>

    <div class="web-line">
      <svg class="contact-icon" viewBox="0 0 24 24" aria-label="Website" fill="none" stroke="#000" stroke-width="1.8"><circle cx="12" cy="12" r="10"/><ellipse cx="12" cy="12" rx="4.5" ry="10"/><path d="M2 12h20M4 7h16M4 17h16"/></svg>
      <span>: www.xxxxxxxxxxxxxxx.xxx</span>
    </div>
  </section>

  <section class="card card--back" aria-label="Business card back">
    <svg class="card-bands" viewBox="0 0 697 408" aria-hidden="true">
      <polygon points="0,0 440,0 320,60 0,60"/>
      <polygon points="377,347 697,347 697,408 253,408"/>
    </svg>
    <div class="brand-name brand-name--large"><span class="brand-dot"></span>Tide Runner</div>
  </section>

</div>
</body>
</html>
```